Wanted: A Simple yet Awesome Blog Hero Image

We need a hero image (blog graphic header) to replace our existing one: https://www.terravexlab.com//blog/soil-classification-foundation-and-pavement-design-starts-here
Want something to reflect what the blog article is about and is a reflection of the title.

Note: we are not in love with any of our hero graphics

Industry/Entity Type

Construction

Colors

Designer to choose colors to be used in the design.

Requirements
Must have
• Width must be 715px
• Height must not exceed 400px
• Content on graphic should be: Soil Classification: Foundation and Pavement Design Starts Here
Nice to have
• a product shown that is mentioned in the blog
Should not have
• a product with a Carrowmere logo

```html
<!DOCTYPE html>
<html lang="en">
<head>
<meta charset="utf-8">
<title>Soil Classification: Foundation and Pavement Design Starts Here</title>
<link href="https://fonts.googleapis.com/css2?family=Exo+2:ital,wght@1,800&family=Ubuntu:wght@300&display=swap" rel="stylesheet">
<style>
  :root {
    --soil-dark: #6e4428;
    --soil-mid: #9c6a44;
    --soil-light: #c08a5c;
    --soil-warm: #b37b50;
    --title-blue: #1f78d1;
    --title-edge: #ffffff;
    --text-white: #ffffff;
    --shadow: rgba(40, 20, 8, 0.75);
  }
  html, body {
    margin: 0;
    padding: 0;
    width: 1200px;
    height: 671px;
    overflow: hidden;
    background: var(--soil-mid);
  }
  .hero {
    position: relative;
    width: 1200px;
    height: 671px;
    overflow: hidden;
  }
  .hero__soil {
    position: absolute;
    inset: 0;
    background:
      radial-gradient(ellipse at 70% 20%, var(--soil-light) 0%, transparent 55%),
      radial-gradient(ellipse at 20% 80%, var(--soil-warm) 0%, transparent 60%),
      linear-gradient(160deg, var(--soil-mid) 0%, var(--soil-warm) 45%, var(--soil-dark) 100%);
  }
  .hero__copy {
    position: absolute;
    left: 0;
    right: 0;
    top: 208px;
    text-align: center;
  }
  .hero__title {
    margin: 0;
    font-family: "Exo 2", sans-serif;
    font-weight: 800;
    font-style: italic;
    font-size: 86px;
    line-height: 1;
    letter-spacing: 1px;
    text-transform: uppercase;
    color: var(--title-blue);
    -webkit-text-stroke: 3px var(--title-edge);
    paint-order: stroke fill;
    text-shadow: 0 0 18px var(--shadow), 2px 3px 6px var(--shadow);
  }
  .hero__subtitle {
    margin: 22px 0 0;
    font-family: "Ubuntu", sans-serif;
    font-weight: 300;
    font-size: 50px;
    line-height: 1.18;
    color: var(--text-white);
    text-shadow: 0 0 14px var(--shadow), 1px 2px 4px var(--shadow);
  }
  .hero__subtitle span { display: block; }
</style>
</head>
<body>
  <header class="hero">
    <div class="hero__soil" role="img" aria-label="Close-up photograph of dry, tilled brown soil with clods and furrows"></div>
    <div class="hero__copy">
      <h1 class="hero__title">Soil Classification:</h1>
      <p class="hero__subtitle">
        <span>Foundation and Pavement Design</span>
        <span>Starts Here</span>
      </p>
    </div>
  </header>
</body>
</html>
```